Velvet Brook is looking for packaging design

We need packaging designs for 5 lines.
Velvet Bloom (pink) - incorporates flowers such as rose, hibiscus, rooibos and fireweed.
Velvet Balance (green) - green tea, comfrey, calendula, dandelion, etc.
Velvet Slumber (lavender) - lavender, violet leaf, orris root, rosemary, chamomile, etc.
Velvet Stillness (blue) - cornflower, seaweed, kelp, etc.
Velvet Star Maiden (white) - white tea, marshmallow, elderflowers, jasmine, etc.

A design is needed for each color so that it can be used for labels on jars and bottles as well as for product boxes. It would be great to see the actual type of flower that is used in the product, incorporated into the design. Additionally, labels will need to be created for the facial steams - Herbal Lumina for mature skin, dry skin, oily skin, and acneic.

We are looking for designs that use flowers, herbs and have a very feminine and expensive feel to it. Preferably an illustration or graphic design versus a photographic print.

It would be a bonus if a tiny fairy could be incorporated into the design somewhere in the picture (not one that stands out but small one that blends in with the background) as well as a crystal (ie. like a little diamond). The logo will be on a black background and the jars/bottles will all be black (examples of the bottle colors have been included as well as the clear glass one for facial steams & bath salts).

Target Market(s)

Sold to high end spas.

Current soap packaging has been attached. I am wondering if someone is able to design a background image that is similar but incorporates the flowers/herbs that are put into the product as well as hiding a tiny fairy and crystal.

Industry/Entity Type

Graphic Design

Requirements
Must have
• 5 product labels or box designs. Flowers and herbs in the graphic design.
A crystal placed somewhere within the background.
A tiny fairy placed somewhere within the background that blends in with the picture. ie. could just be the outline of a fairy or it could be the same color as the background.
Nice to have
• A herbal/flower background for steams.

```html
<!DOCTYPE html>
<html lang="en">
<head>
<meta charset="utf-8">
<title>Velvet Bloom – Label Designs</title>
<link rel="stylesheet" href="https://fonts.googleapis.com/css2?family=Cinzel:wght@500&family=Didact+Gothic&display=swap">
<style>
  :root {
    --page: #ffffff;
    --ink-white: #ffffff;
    --label-black: #050505;
    --kraft: #b58d5c;
    --kraft-light: #c39c6a;
    --bloom-pink: #e23a98;
    --bloom-coral: #ef6f6a;
    --bloom-blush: #f3bfb2;
    --bloom-gold: #d6a52c;
    --bloom-leaf: #4d6661;
    --frame-magenta: #c42c86;
  }

  * { margin: 0; padding: 0; box-sizing: border-box; }

  html, body {
    width: 846px;
    height: 1200px;
    overflow: hidden;
    background: var(--page);
  }

  .canvas {
    position: relative;
    width: 846px;
    height: 1200px;
    background: var(--page);
  }

  .label {
    position: absolute;
    width: 473px;
    height: 473px;
  }

  .label--kraft { left: 185px; top: 51px; }
  .label--black { left: 189px; top: 613px; }

  .floral-field {
    position: absolute;
    inset: 0;
    background:
      radial-gradient(ellipse 70% 45% at 50% 0%, rgba(226, 58, 152, 0.75), transparent 75%),
      radial-gradient(ellipse 45% 60% at 100% 60%, rgba(239, 111, 106, 0.7), transparent 75%),
      radial-gradient(ellipse 45% 60% at 0% 45%, rgba(214, 165, 44, 0.55), transparent 75%),
      radial-gradient(ellipse 70% 40% at 50% 100%, rgba(243, 191, 178, 0.55), transparent 75%),
      var(--label-black);
  }

  .panel {
    position: absolute;
    border: 3px solid var(--ink-white);
    border-radius: 8px;
    box-shadow: 0 0 0 3px var(--frame-magenta), 0 0 10px 4px rgba(196, 44, 134, 0.6);
    text-align: center;
    color: var(--ink-white);
  }

  .label--kraft .panel {
    left: 80px; top: 66px; width: 318px; height: 318px;
    background: repeating-linear-gradient(90deg, var(--kraft) 0 3px, var(--kraft-light) 3px 5px);
  }

  .label--black .panel {
    left: 84px; top: 66px; width: 313px; height: 318px;
    background: var(--label-black);
  }

  .brand {
    position: absolute;
    left: 0; right: 0;
    top: 18px;
    display: flex;
    flex-direction: column;
    align-items: center;
    gap: 8px;
  }

  .brand-dot {
    width: 18px; height: 18px;
    border-radius: 50%;
    background: var(--ink-white);
  }

  .brand-name {
    font-family: "Cinzel", serif;
    font-weight: 500;
    font-size: 15px;
    letter-spacing: 0.3px;
    text-transform: uppercase;
    white-space: nowrap;
  }

  .product-name {
    position: absolute;
    left: 0; right: 0;
    top: 136px;
    font-family: "Didact Gothic", sans-serif;
    font-size: 44px;
    font-weight: 400;
    line-height: 1;
    white-space: nowrap;
    word-spacing: -2px;
  }

  .fairy-mark {
    position: absolute;
    left: 50%;
    bottom: 10px;
    width: 30px;
    height: 56px;
    margin-left: -15px;
    border-radius: 45% 45% 30% 30%;
    background: rgba(255, 255, 255, 0.85);
  }

  .label--black .fairy-mark { background: rgba(255, 255, 255, 0.3); }
</style>
</head>
<body>
<main class="canvas">

  <section class="label label--kraft">
    <div class="floral-field" role="img" aria-label="Painted pattern of pink and coral roses, yellow blossoms and grey-green leaves on black"></div>
    <div class="panel">
      <div class="brand">
        <span class="brand-dot"></span>
        <span class="brand-name">Velvet Brook</span>
      </div>
      <h1 class="product-name">Velvet Bloom</h1>
      <div class="fairy-mark" role="img" aria-label="Small white fairy silhouette"></div>
    </div>
  </section>

  <section class="label label--black">
    <div class="floral-field" role="img" aria-label="Painted pattern of pink and coral roses, yellow blossoms and grey-green leaves on black"></div>
    <div class="panel">
      <div class="brand">
        <span class="brand-dot"></span>
        <span class="brand-name">Velvet Brook</span>
      </div>
      <h2 class="product-name">Velvet Bloom</h2>
      <div class="fairy-mark" role="img" aria-label="Faint grey fairy silhouette"></div>
    </div>
  </section>

</main>
</body>
</html>
```